Lumen Keyvault Password Manager WebApp Design

Lumen Keyvault is seeking an expert UI designer to provide a fresh and modern visual appeal for our product. Our inspiration comes from two major tools that have successfully managed to balance functionality and design aesthetics - Orbix Folder and Vaultmint. We want our application to exude a similar trustworthiness and modernity, through a clean, intuitive and responsive design.
We have established preliminary mockups and would like the designer to work within these parameters while enhancing the overall user experience. The primary tasks will involve innovative and improved designs of the login screen and the password screen, both being crucial touchpoints for our users. The login screen also serves a crucial role in demonstrating how our system works.
Key Elements:
Logo Integration: We are providing the logo for Lumen Keyvault. The design should align with the logo, both in terms of colors and overall aesthetic, to ensure a cohesive brand identity.
Color Palette: The UI design should adhere to the color palette derived from the logo to maintain brand consistency. The design should effectively utilize these colors to highlight important elements and improve user engagement.
Trustworthy and Modern Design: The UI should be professional and trustworthy. It should mirror the look and feel of Orbix Folder's simplicity and Vaultmint's solid security design, which inspires user confidence.
Adherence to Mockup Boundaries: The existing mockups serve as a guideline for the layout and placement of elements. The design should respect these boundaries while bringing innovation and visual appeal.
Improved Login Screen: The login screen is a key part of the user's journey and should be designed with utmost care. It should be intuitive, easy-to-use, visually engaging, and educative, showcasing how the system operates and encouraging users to sign in with confidence.
Enhanced Password Screen: The password screen, another key user touchpoint, needs improvement. The different types of passwords should be made more visible and intuitive, easing user interaction and enhancing the overall experience.
Prospective designers are encouraged to test our current version available for free at app.lumenkeyvault.com to understand the product better and contribute to meaningful design enhancements.
The goal of this project is to provide a visually compelling and user-friendly interface for Lumen Keyvault that inspires user trust, while adhering to the branding elements, including color scheme and logo design. The ideal designer will have a proven track record of creating compelling UI designs that enhance user experience and engagement.
We preferred the design to be in Figma.
Please provide the 3 design so we can evaluate if we like to choice you:
1. Login Page.
2. Passwords View design
3. Single Passwod Page
We need all the pages to be design that are provided as screenshots.

```html
<!DOCTYPE html>
<html lang="en">
<head>
<meta charset="utf-8">
<title>Lumen Keyvault – Login, Vault and Password Detail</title>
<link href="https://fonts.googleapis.com/css2?family=Montserrat:wght@400;500;600;700;800&display=swap" rel="stylesheet">
<style>
  :root{
    --board:#ebebeb;
    --screen:#f4f9fd;
    --white:#ffffff;
    --ink:#1f2330;
    --muted:#6d7480;
    --soft:#c7ccd3;
    --line:#e3e8ee;
    --blue:#1e9af5;
    --pink:#f0486e;
    --green:#4fdc8f;
    --gold:#ffbc00;
    --navy:#1b2a8a;
    --save:#e2e4e8;
  }
  *{box-sizing:border-box;margin:0;padding:0}
  html,body{width:743px;height:1200px;overflow:hidden;background:var(--board);font-family:"Montserrat",sans-serif;color:var(--ink)}
  .screen{position:absolute;left:57px;width:629px;height:354px;background:var(--screen);overflow:hidden}
  .abs{position:absolute}
  .center-x{transform:translateX(-50%);white-space:nowrap;text-align:center}

  /* ---------- Login ---------- */
  .login .welcome{left:314px;top:48px;font-size:7.5px;font-weight:600;color:var(--muted)}
  .login .welcome-rule{left:306px;top:59px;width:16px;height:1.5px;background:var(--soft);border-radius:1px}
  .login .brand{left:314px;top:66px;display:flex;align-items:center;gap:6px;font-size:13px;font-weight:500}
  .brand-square{width:12px;height:12px;background:var(--blue);border-radius:2px;flex:none}
  .login .hero-art{left:154px;top:112px;width:143px;height:116px;border-radius:10px;
    background:radial-gradient(circle at 55% 50%, #3b4fc4 0%, #1b2a8a 38%, #b9c9f7 62%, #eef3fb 80%)}
  .login .caption{left:224px;top:238px;font-size:5.6px;line-height:7px;color:var(--muted)}
  .login .caption b{color:#44494f;font-weight:700}
  .login .dots{left:209px;top:264px;display:flex;gap:5.5px}
  .login .dots span{width:4.5px;height:4.5px;border-radius:50%;background:var(--soft)}
  .login .dots span.on{background:var(--blue)}
  .login .flow-pill{left:354px;top:133px;width:73px;height:27px;border-radius:14px;background:var(--white);
    box-shadow:0 2px 6px rgba(30,60,120,.08);display:flex;align-items:center;justify-content:center;gap:6px}
  .flow-pill .sq{width:12px;height:12px;background:var(--blue);border-radius:2px}
  .flow-pill .ci{width:13px;height:13px;background:var(--green);border-radius:50%}
  .login .kicker{left:354px;top:167px;font-size:14px;font-weight:500;color:#7c8088;letter-spacing:-.2px}
  .login .headline{left:353px;top:179px;font-size:24.5px;font-weight:800;color:#7c8088;letter-spacing:-.3px}
  .login .subline{left:354px;top:204px;font-size:8.3px;font-weight:500;color:#7c8088}
  .login .subline b{font-weight:700}
  .login .signin{left:356px;top:234px;width:139px;height:17px;border:1px solid var(--blue);border-radius:3px;background:var(--white);
    display:flex;align-items:center;justify-content:center;gap:5px;font-size:5.6px;font-weight:500;color:var(--blue)}
  .signin .dot{width:7px;height:7px;border-radius:50%;background:var(--blue)}
  .login .footer-rule{left:134px;top:331px;width:361px;height:1px;background:var(--line)}
  .login .legal{left:314px;top:340px;font-size:3.9px;color:var(--muted)}
  .login .legal a{color:var(--blue);text-decoration:none}

  /* ---------- App shell ---------- */
  .tab-indicator{left:382px;top:0;width:28px;height:3.5px;background:var(--blue);border-radius:0 0 3px 3px}
  .app-brand{left:11px;top:12px;display:flex;align-items:center;gap:4px;font-size:6.6px;font-weight:500}
  .app-brand .brand-square{width:9px;height:9px}
  .nav{top:12px;display:flex;align-items:center;gap:4px;font-size:5.5px;color:#8a9099}
  .nav svg{width:10px;height:10px;stroke:#6f7680;fill:none;stroke-width:1.6}
  .nav.active{color:var(--blue);font-weight:600}
  .nav.active svg{stroke:var(--blue)}
  .nav .badge{position:absolute;left:5px;top:-1px;width:5px;height:5px;border-radius:50%;background:var(--gold);font-size:3.5px;line-height:5px;text-align:center;color:var(--ink);font-weight:700}
  .avatar{left:582px;top:8px;width:19px;height:19px;border-radius:50%;border:1.5px solid var(--blue);
    background:radial-gradient(circle at 50% 40%,#d9a98a 0%,#8a5a44 55%,#3b4a5c 100%)}
  .chev{left:605px;top:14px;width:7px;height:7px;stroke:var(--ink);fill:none;stroke-width:1.6}
  .grid-pill{left:8px;top:36px;width:25px;height:24px;border-radius:12px;background:var(--white);display:flex;align-items:center;justify-content:center}
  .grid-pill svg{width:9px;height:9px;stroke:var(--blue);fill:none;stroke-width:1.3}
  .search{left:42px;top:36px;width:489px;height:24px;border-radius:12px;background:var(--white);display:flex;align-items:center;justify-content:space-between;padding:0 10px 0 10px}
  .search .label{font-size:7px;font-weight:600;color:var(--blue)}
  .search svg{width:7px;height:7px;stroke:var(--blue);fill:none;stroke-width:2}
  .add-btn{left:538px;top:36px;width:83px;height:24px;border-radius:12px;background:var(--blue);color:var(--white);
    font-size:6px;font-weight:600;display:flex;align-items:center;justify-content:center;gap:4px}
  .add-btn svg{width:7px;height:7px;stroke:var(--white);stroke-width:1.6}
  .sidebar{left:8px;top:71px;width:25px;height:206px;border-radius:12px;background:var(--white);display:flex;flex-direction:column;align-items:center;padding-top:9px;gap:9.7px}
  .sidebar svg{width:8px;height:8px;fill:none;stroke:#5f6670;stroke-width:1.5;stroke-linecap:round;stroke-linejoin:round;flex:none}
  .sidebar svg.current{stroke:var(--blue)}
  .sidebar .plus{position:absolute;left:5px;bottom:3.5px;width:15px;height:15px;border-radius:50%;background:var(--blue);display:flex;align-items:center;justify-content:center}
  .sidebar .plus svg{stroke:var(--white);width:7px;height:7px;stroke-width:2}

  .card{position:absolute;width:137px;height:25.5px;border-radius:12px;background:var(--white);border:1px solid transparent;
    display:flex;align-items:center;padding-left:5px;font-size:5.4px;color:#3c424b}
  .card .grip{width:3px;height:9px;margin-right:5px;background-image:radial-gradient(circle,#d5d9de 0.6px,transparent 0.7px);background-size:1.5px 1.5px}
  .card .mark{width:10px;height:10px;border-radius:50%;flex:none}
  .card .mark.square{border-radius:2px}
  .card .name{flex:1;margin-left:7px;white-space:nowrap}
  .card svg.star{width:8px;height:8px;flex:none;fill:none;stroke:var(--soft);stroke-width:1.4}
  .card svg.star.on{fill:var(--gold);stroke:var(--gold)}
  .card svg.env{width:10px;height:8px;fill:none;stroke:var(--ink);stroke-width:1.3}
  .card .status{width:5px;height:5px;border-radius:50%;background:#d6dade;margin:0 8px 0 6px;flex:none}
  .card.pink{border-color:var(--pink)} .card.pink .name{color:var(--pink)} .card.pink .status{background:var(--pink)}
  .card.green{border-color:var(--green)} .card.green .name{color:var(--green)} .card.green .status{background:var(--green)}
  .card.mail{border-color:var(--blue)} .card.mail .name{color:var(--blue)} .card.mail .status{background:var(--blue)}
  .card.selected{border:2px solid var(--blue)}

  .scroll{left:470px;top:71px;width:1.5px;height:272px;background:var(--line)}
  .scroll::before{content:"";position:absolute;left:0;top:0;width:1.5px;height:67px;background:var(--blue);border-radius:1px}
  .detail{left:480px;width:141px;border-radius:12px;background:var(--white)}

  /* empty detail */
  .empty .pw-pill{left:48px;top:69px;width:44px;height:13px;border:1.5px solid var(--soft);border-radius:7px;display:flex;align-items:center;justify-content:center;gap:2.5px;color:var(--gold);font-size:6px;font-weight:700}
  .empty .hand{left:64px;top:86px;width:10px;height:11px;fill:none;stroke:var(--blue);stroke-width:1.2}
  .empty .title{left:70.5px;top:107px;font-size:10.4px;font-weight:600}
  .empty .sub{left:70.5px;top:121px;font-size:6px;color:#3c424b}
  .empty .activate{left:70.5px;top:175px;font-size:6.6px;font-weight:700;color:var(--blue)}
  .empty .tfa{left:70.5px;top:190px;font-size:6px;color:var(--muted)}
  .empty .secure{left:36px;top:203px;width:68px;height:13px;border-radius:7px;background:var(--green);color:var(--white);font-size:5.6px;font-weight:500;display:flex;align-items:center;justify-content:center}

  /* filled detail */
  .info .tab-on{left:7px;top:6px;width:64px;height:17px;border-radius:9px;background:var(--blue);color:var(--white);font-size:5.2px;font-weight:600;display:flex;align-items:center;justify-content:center;gap:4px}
  .info .tab-on svg{width:8px;height:7px;fill:none;stroke:var(--white);stroke-width:1.3}
  .info .tab-off{left:88px;top:6px;height:17px;display:flex;align-items:center;gap:5px;font-size:5.2px;color:var(--muted)}
  .info .tab-off svg,.info .field svg,.info .copy,.info .eye{fill:none;stroke:#6f7680;stroke-width:1.2}
  .info .tab-off svg{width:8px;height:8px}
  .info .account{left:10px;top:39px;display:flex;align-items:center;gap:5px;font-size:8.4px;font-weight:600;color:var(--blue)}
  .info .account .mark{width:10px;height:10px;border-radius:50%;background:var(--ink)}
  .info .field{left:9px;display:flex;align-items:center;gap:4px;font-size:6px;font-weight:500;color:var(--blue)}
  .info .field svg{width:7px;height:7px;stroke:var(--blue)}
  .info .value{left:8px;font-size:6px;color:#3c424b;white-space:nowrap}
  .info .copy{left:124px;width:8px;height:8px}
  .info .eye{left:124px;width:8px;height:7px}
  .info .rule{left:8px;width:123px;height:1px;background:var(--line)}
  .info .edit{left:25px;top:186px;width:90px;height:18px;border-radius:9px;background:var(--blue);color:var(--white);font-size:6px;font-weight:600;display:flex;align-items:center;justify-content:center}
  .info .save{left:25px;top:207px;width:90px;height:18px;border-radius:9px;background:var(--save);color:#8a9099;font-size:6px;font-weight:500;display:flex;align-items:center;justify-content:center}
</style>
</head>
<body>

<svg width="0" height="0" style="position:absolute" aria-hidden="true">
  <defs>
    <symbol id="i-star" viewBox="0 0 24 24"><path d="M12 2.5l2.9 6.1 6.6.8-4.9 4.6 1.3 6.6L12 17.3l-5.9 3.3 1.3-6.6-4.9-4.6 6.6-.8z"/></symbol>
    <symbol id="i-key" viewBox="0 0 24 24"><circle cx="7" cy="16" r="4.5"/><path d="M10.5 12.5L20 3M16 7l3 3M14 9l2 2"/></symbol>
    <symbol id="i-folder" viewBox="0 0 24 24"><path d="M3 6h7l2 2h9v11H3z"/></symbol>
    <symbol id="i-share" viewBox="0 0 24 24"><circle cx="6" cy="12" r="3"/><circle cx="18" cy="5" r="3"/><circle cx="18" cy="19" r="3"/><path d="M8.6 10.5l6.8-4M8.6 13.5l6.8 4"/></symbol>
    <symbol id="i-case" viewBox="0 0 24 24"><rect x="3" y="7" width="18" height="13" rx="2"/><path d="M9 7V4h6v3M9 7v13M15 7v13"/></symbol>
    <symbol id="i-chat" viewBox="0 0 24 24"><path d="M4 5h16v11H9l-5 4z"/></symbol>
    <symbol id="i-cart" viewBox="0 0 24 24"><path d="M2 3h3l3 12h11l2-8H6"/><circle cx="9" cy="20" r="1.5"/><circle cx="18" cy="20" r="1.5"/></symbol>
    <symbol id="i-compass" viewBox="0 0 24 24"><circle cx="12" cy="12" r="9.5"/><path d="M15.5 8.5l-2 5-5 2 2-5z"/></symbol>
    <symbol id="i-dollar" viewBox="0 0 24 24"><path d="M12 2v20M17 6H10a3 3 0 000 6h4a3 3 0 010 6H6"/></symbol>
    <symbol id="i-mail" viewBox="0 0 24 24"><rect x="2.5" y="5" width="19" height="14" rx="2"/><path d="M3 6l9 7 9-7"/></symbol>
    <symbol id="i-plus" viewBox="0 0 24 24"><path d="M12 4v16M4 12h16"/></symbol>
    <symbol id="i-home" viewBox="0 0 24 24"><path d="M3 11l9-8 9 8v10H3z"/></symbol>
    <symbol id="i-team" viewBox="0 0 24 24"><circle cx="9" cy="8" r="4"/><path d="M2 21c0-4 3-7 7-7s7 3 7 7"/><circle cx="17" cy="7" r="3"/><path d="M18 13c2.5.5 4 3 4 6"/></symbol>
    <symbol id="i-bell" viewBox="0 0 24 24"><path d="M6 17V11a6 6 0 0112 0v6l2 2H4zM10 21h4"/></symbol>
    <symbol id="i-list" viewBox="0 0 24 24"><path d="M8 6h13M8 12h13M8 18h13M3 6h1M3 12h1M3 18h1"/></symbol>
    <symbol id="i-copy" viewBox="0 0 24 24"><rect x="8" y="8" width="13" height="13" rx="2"/><path d="M16 8V3H3v13h5"/></symbol>
    <symbol id="i-grid" viewBox="0 0 24 24"><rect x="3" y="3" width="7" height="7" rx="2"/><rect x="14" y="3" width="7" height="7" rx="2"/><rect x="3" y="14" width="7" height="7" rx="2"/><rect x="14" y="14" width="7" height="7" rx="2"/></symbol>
  </defs>
</svg>

<!-- ================= Login ================= -->
<section class="screen login" style="top:47px">
  <div class="abs welcome center-x">Welcome to</div>
  <div class="abs welcome-rule"></div>
  <div class="abs brand center-x"><span class="brand-square"></span>Lumen Keyvault</div>

  <div class="abs hero-art" role="img" aria-label="Illustration of a person holding a key beside a monitor guarded by a shield, with a password field and server stacks"></div>
  <p class="abs caption center-x">Only you from your browser can connect to your Orbix Folder™.<br><b>We do not have any access to it.</b></p>
  <div class="abs dots"><span class="on"></span><span></span><span></span></div>

  <div class="abs flow-pill">
    <span class="sq"></span>
    <svg width="6" height="5" viewBox="0 0 12 10" fill="none" stroke="#6f7680" stroke-width="1.4"><path d="M1 5h10M7 1l4 4-4 4"/></svg>
    <span class="ci"></span>
  </div>
  <div class="abs kicker">ENCRYPTED</div>
  <div class="abs headline">PASSWORDS</div>
  <div class="abs subline">DIRECTLY ON YOUR <b>ORBIX</b> FOLDER</div>
  <div class="abs signin"><span class="dot"></span>Sign In with Orbix</div>

  <div class="abs footer-rule"></div>
  <p class="abs legal center-x">By clicking login , you agree with our <a href="#">Term of use</a>. Learn what data we collect and how we handle it in our <a href="#">privacy policy</a>.</p>
</section>

<!-- ================= Vault: nothing selected ================= -->
<section class="screen app" style="top:417px">
  <div class="abs tab-indicator"></div>
  <div class="abs app-brand"><span class="brand-square"></span>Lumen Keyvault</div>
  <div class="abs nav active" style="left:380px"><svg><use href="#i-home"/></svg>Vault</div>
  <div class="abs nav" style="left:422px"><svg><use href="#i-team"/></svg>Teams</div>
  <div class="abs nav" style="left:469px"><svg><use href="#i-bell"/></svg><span class="badge">5</span>Activity</div>
  <div class="abs nav" style="left:517px"><svg><use href="#i-list"/></svg>More</div>
  <div class="abs avatar" role="img" aria-label="User profile photo"></div>
  <svg class="abs chev" viewBox="0 0 12 12"><path d="M2 4l4 4 4-4"/></svg>

  <div class="abs grid-pill"><svg><use href="#i-grid"/></svg></div>
  <div class="abs search"><span class="label">All Password</span><svg viewBox="0 0 24 24"><circle cx="10" cy="10" r="7"/><path d="M15 15l6 6"/></svg></div>
  <div class="abs add-btn"><svg><use href="#i-plus"/></svg>Add Password</div>

  <nav class="abs sidebar">
    <svg class="current"><use href="#i-key"/></svg><svg><use href="#i-star"/></svg><svg><use href="#i-folder"/></svg><svg><use href="#i-share"/></svg><svg><use href="#i-case"/></svg><svg><use href="#i-chat"/></svg><svg><use href="#i-cart"/></svg><svg><use href="#i-compass"/></svg><svg><use href="#i-dollar"/></svg><svg><use href="#i-mail"/></svg>
    <span class="plus"><svg><use href="#i-plus"/></svg></span>
  </nav>

  <div class="card pink" style="left:42px;top:71px"><span class="grip"></span><span class="mark square" style="background:var(--blue)"></span><span class="name">Test</span><svg class="star on"><use href="#i-star"/></svg><span class="status"></span></div>
  <div class="card" style="left:184px;top:71px"><span class="grip"></span><span class="mark" style="background:#ff5a1f"></span><span class="name">Threadly</span><svg class="star"><use href="#i-star"/></svg><span class="status"></span></div>
  <div class="card green" style="left:326px;top:71px"><span class="grip"></span><span class="mark square" style="background:#f7c948"></span><span class="name">Cartwave</span><svg class="star on"><use href="#i-star"/></svg><span class="status"></span></div>
  <div class="card" style="left:42px;top:101px"><span class="grip"></span><span class="mark" style="background:var(--ink)"></span><span class="name">Marketon</span><svg class="star"><use href="#i-star"/></svg><span class="status"></span></div>
  <div class="card" style="left:184px;top:101px"><span class="grip"></span><span class="mark" style="background:#b9bdc2"></span><span class="name">Knowpedia</span><svg class="star on"><use href="#i-star"/></svg><span class="status"></span></div>
  <div class="card" style="left:326px;top:101px"><span class="grip"></span><span class="mark square" style="background:var(--ink)"></span><span class="name">Lockra</span><svg class="star"><use href="#i-star"/></svg><span class="status"></span></div>
  <div class="card" style="left:42px;top:130px"><span class="grip"></span><span class="mark" style="background:var(--blue)"></span><span class="name">Chirpline</span><svg class="star"><use href="#i-star"/></svg><span class="status"></span></div>
  <div class="card mail" style="left:184px;top:130px"><span class="grip"></span><svg class="env"><use href="#i-mail"/></svg><span class="name">sam@lumenkeyvault.com</span><svg class="star"><use href="#i-star"/></svg><span class="status"></span></div>
  <div class="card" style="left:326px;top:130px"><span class="grip"></span><span class="mark square" style="background:#2f79c8"></span><span class="name">Kontak</span><svg class="star"><use href="#i-star"/></svg><span class="status"></span></div>
  <div class="card green" style="left:42px;top:160px"><span class="grip"></span><span class="mark" style="background:#1b5c8a"></span><span class="name">Craft Crowd</span><svg class="star on"><use href="#i-star"/></svg><span class="status"></span></div>

  <div class="abs scroll"></div>

  <aside class="abs detail empty" style="top:74px;height:270px">
    <div class="abs pw-pill">*&nbsp;*&nbsp;*&nbsp;*&nbsp;*</div>
    <svg class="abs hand" viewBox="0 0 20 22"><path d="M7 11V3a1.5 1.5 0 013 0v7M10 9.5a1.5 1.5 0 013 0v1.5M13 10.5a1.5 1.5 0 013 0v5c0 3-2 5-5 5H10c-2 0-3-1-4-2.5L3 14a1.4 1.4 0 012-2l2 2"/></svg>
    <div class="abs title center-x">Select password to</div>
    <div class="abs sub center-x">view details, edit and give access</div>
    <div class="abs activate center-x">Activate</div>
    <div class="abs tfa center-x">2 Factor Authentication</div>
    <div class="abs secure">Secure Now</div>
  </aside>
</section>

<!-- ================= Vault: single password ================= -->
<section class="screen app" style="top:783px">
  <div class="abs tab-indicator"></div>
  <div class="abs app-brand"><span class="brand-square"></span>Lumen Keyvault</div>
  <div class="abs nav active" style="left:380px"><svg><use href="#i-home"/></svg>Vault</div>
  <div class="abs nav" style="left:422px"><svg><use href="#i-team"/></svg>Teams</div>
  <div class="abs nav" style="left:469px"><svg><use href="#i-bell"/></svg><span class="badge">5</span>Activity</div>
  <div class="abs nav" style="left:517px"><svg><use href="#i-list"/></svg>More</div>
  <div class="abs avatar" role="img" aria-label="User profile photo"></div>
  <svg class="abs chev" viewBox="0 0 12 12"><path d="M2 4l4 4 4-4"/></svg>

  <div class="abs grid-pill"><svg><use href="#i-grid"/></svg></div>
  <div class="abs search"><span class="label">All Password</span><svg viewBox="0 0 24 24"><circle cx="10" cy="10" r="7"/><path d="M15 15l6 6"/></svg></div>
  <div class="abs add-btn"><svg><use href="#i-plus"/></svg>Add Password</div>

  <nav class="abs sidebar">
    <svg class="current"><use href="#i-key"/></svg><svg><use href="#i-star"/></svg><svg><use href="#i-folder"/></svg><svg><use href="#i-share"/></svg><svg><use href="#i-case"/></svg><svg><use href="#i-chat"/></svg><svg><use href="#i-cart"/></svg><svg><use href="#i-compass"/></svg><svg><use href="#i-dollar"/></svg><svg><use href="#i-mail"/></svg>
    <span class="plus"><svg><use href="#i-plus"/></svg></span>
  </nav>

  <div class="card pink" style="left:42px;top:71px"><span class="grip"></span><span class="mark square" style="background:var(--blue)"></span><span class="name">Test</span><svg class="star on"><use href="#i-star"/></svg><span class="status"></span></div>
  <div class="card" style="left:184px;top:71px"><span class="grip"></span><span class="mark" style="background:#ff5a1f"></span><span class="name">Threadly</span><svg class="star"><use href="#i-star"/></svg><span class="status"></span></div>
  <div class="card green" style="left:326px;top:71px"><span class="grip"></span><span class="mark square" style="background:#f7c948"></span><span class="name">Cartwave</span><svg class="star on"><use href="#i-star"/></svg><span class="status"></span></div>
  <div class="card selected" style="left:42px;top:101px"><span class="grip"></span><span class="mark" style="background:var(--ink)"></span><span class="name">Marketon</span><svg class="star"><use href="#i-star"/></svg><span class="status"></span></div>
  <div class="card" style="left:184px;top:101px"><span class="grip"></span><span class="mark" style="background:#b9bdc2"></span><span class="name">Knowpedia</span><svg class="star on"><use href="#i-star"/></svg><span class="status"></span></div>
  <div class="card" style="left:326px;top:101px"><span class="grip"></span><span class="mark square" style="background:var(--ink)"></span><span class="name">Lockra</span><svg class="star"><use href="#i-star"/></svg><span class="status"></span></div>
  <div class="card" style="left:42px;top:130px"><span class="grip"></span><span class="mark" style="background:var(--blue)"></span><span class="name">Chirpline</span><svg class="star"><use href="#i-star"/></svg><span class="status"></span></div>
  <div class="card mail" style="left:184px;top:130px"><span class="grip"></span><svg class="env"><use href="#i-mail"/></svg><span class="name">sam@lumenkeyvault.com</span><svg class="star"><use href="#i-star"/></svg><span class="status"></span></div>
  <div class="card" style="left:326px;top:130px"><span class="grip"></span><span class="mark square" style="background:#2f79c8"></span><span class="name">Kontak</span><svg class="star"><use href="#i-star"/></svg><span class="status"></span></div>
  <div class="card green" style="left:42px;top:160px"><span class="grip"></span><span class="mark" style="background:#1b5c8a"></span><span class="name">Craft Crowd</span><svg class="star on"><use href="#i-star"/></svg><span class="status"></span></div>

  <div class="abs scroll"></div>

  <aside class="abs detail info" style="top:72px;height:269px">
    <div class="abs tab-on"><svg viewBox="0 0 24 20"><path d="M2 3h8a2 2 0 012 2v13a2 2 0 00-2-2H2zM22 3h-8a2 2 0 00-2 2v13a2 2 0 012-2h8z"/></svg>Information</div>
    <div class="abs tab-off"><svg><use href="#i-key"/></svg>Access</div>

    <div class="abs account"><span class="mark"></span>Marketon Account</div>

    <div class="abs field" style="top:74px"><svg><use href="#i-mail"/></svg>Email</div>
    <svg class="abs copy" style="top:74px"><use href="#i-copy"/></svg>
    <div class="abs value" style="top:87px">sam@lumenkeyvault.com</div>
    <div class="abs rule" style="top:102px"></div>

    <div class="abs field" style="top:111px"><svg><use href="#i-key"/></svg>Password</div>
    <svg class="abs copy" style="top:111px"><use href="#i-copy"/></svg>
    <div class="abs value" style="top:122px;letter-spacing:1.2px;font-weight:700">••••••••••••</div>
    <svg class="abs eye" style="top:124px" viewBox="0 0 24 18"><path d="M1 9s4-7 11-7 11 7 11 7-4 7-11 7S1 9 1 9z"/><circle cx="12" cy="9" r="3"/></svg>
    <div class="abs rule" style="top:138px"></div>

    <div class="abs field" style="top:147px"><svg viewBox="0 0 24 24"><path d="M20 11l-8.5 8.5a5 5 0 01-7-7L13 4a3.3 3.3 0 014.7 4.7L9.2 17.2a1.7 1.7 0 01-2.4-2.4L14.5 7"/></svg>Note</div>
    <svg class="abs copy" style="top:147px"><use href="#i-copy"/></svg>
    <div class="abs value" style="top:160px">1213524613235431216111135428q</div>

    <div class="abs edit">Edit / Add custom field</div>
    <div class="abs save">Save</div>
  </aside>
</section>

</body>
</html>
```